Thornbeck Advisory Group Business Card Design Project

2-sided business card for my small (me and a couple subcontractors) firm, which consults to public community colleges and school districts and public agencies in California on energy matters, mostly solar electric systems that can reduce their electricity use by as much as 80%. I prepare requests for proposals (RFPs), manage the RFP processes, and work with the solar vendors to get the best deal for my clients. I also do regulatory and legislative advocacy for strong renewable energy policies. I do lots of quantitative analysis to make sure the solar systems are sized to produce the maximum monetary savings and focus a lot on the aesthetic design of the solar systems, as architectural features of the campuses (most are carport structures built in parking lots, but some are built on the ground and on rooftops). All my work is geared to getting the best value, highest quality, and most reliable solar system. My career background is in public interest energy advocacy; I'm not a consultant trying to make a million dollars but someone who is still serving in the public interest.

My competition is made up of much larger firms; this business card/logo in large part is intended to present an image of my firm as an equal to these larger firms despite my smaller size.

Essential information as follows:
Firm name: Thornbeck Advisory Group
Tagline: Clean Energy Procurement for the Public Sector
Name: Walter Pennick
email, 2 phone number, and address listed as well.

Target Market(s)

Public schools, community colleges, & public agencies.There is a wide range in the sophistication of these organizations.

Industry/Entity Type

Parking

Requirements
Must have
• - several rich colors, which can be either in the logo or in the background - the overall feeling of the card should reflect richness of color. I have uploaded some photos showing some colors that I like together. By rich I do not necessarily mean bright. I suppose bright colors in the logo could be supported with rich colors in the overall background of the card.
- professional, and powerful in an understated way (not kooky, cartoonish, or very playful)
- the logo must NOT be too representational of solar energy or the sun, but at the same time it would be good for the logo to be somewhat suggestive of this.

Nice to have
• -I like abstract and geometric images (with rich colts).
- A very subtle reference to schools/colleges/education would be great but it CANNOT be explicit; it would have to be faintly suggestive.
- In the logo I like the idea of abstract or geometric shapes intersecting with other in an interesting and suggestive way, conveying the multiple aspects of my practice (economics, data analysis, energy analysis, problem solving, managing collaborative processes, policy analysis)
- My work relates to environmental concerns, especially climate change. Working this into the logo in a subtle way could be good, but it's not a requirement.
- I like the idea that the logo/card feels serene.
- In designing the business card, I kind of like the idea of having the tag line as the first thing they read, then they see the firm name.

Should not have
• Not:
- humorous
- boring
- overly slick
- overly formal
- whimsical

```html
<!DOCTYPE html>
<html lang="en">
<head>
<meta charset="utf-8">
<title>Thornbeck Advisory Group – Business Card</title>
<link rel="stylesheet" href="https://fonts.googleapis.com/css2?family=Oswald:wght@300;400&family=Nunito:wght@700;800&display=swap">
<style>
  :root {
    --page: #ebe8e4;
    --ink-light: #ffffff;
    --ink-shadow: rgba(20, 8, 30, 0.85);
    --back-dark: #2b2a1e;
    --back-olive: #4a4424;
    --back-plum: #5a2f6a;
    --back-violet: #8a4fa8;
    --front-amber: #d9780f;
    --front-gold: #f2b233;
    --front-teal: #5a9c95;
    --front-magenta: #b32fb5;
    --front-violet: #7b2c9c;
    --front-deep: #3a1e3c;
  }
  * { margin: 0; padding: 0; box-sizing: border-box; }
  html, body {
    width: 1200px; height: 900px; overflow: hidden;
    background: var(--page);
  }
  .sheet {
    width: 1200px; height: 900px;
    display: flex; flex-direction: column; align-items: center; justify-content: center;
    gap: 40px;
  }
  .card {
    position: relative;
    width: 700px; height: 400px;
    border-radius: 4px;
    overflow: hidden;
    box-shadow: 0 6px 18px rgba(0,0,0,0.25);
  }
  .card__backdrop { position: absolute; inset: 0; }
  .card--back .card__backdrop {
    background:
      radial-gradient(ellipse at 80% 15%, var(--back-violet) 0%, transparent 55%),
      radial-gradient(ellipse at 20% 85%, #6b6a58 0%, transparent 45%),
      radial-gradient(ellipse at 40% 55%, var(--back-olive) 0%, transparent 60%),
      linear-gradient(120deg, var(--back-dark) 0%, #3a3526 45%, var(--back-plum) 100%);
  }
  .card--front .card__backdrop {
    background:
      radial-gradient(ellipse at 22% 30%, var(--front-gold) 0%, transparent 40%),
      radial-gradient(ellipse at 12% 85%, var(--front-teal) 0%, transparent 40%),
      radial-gradient(ellipse at 85% 35%, var(--front-magenta) 0%, transparent 50%),
      radial-gradient(ellipse at 55% 80%, var(--front-deep) 0%, transparent 50%),
      linear-gradient(100deg, var(--front-amber) 0%, #8a3d2a 45%, var(--front-violet) 100%);
  }
  .brand {
    position: absolute;
    display: flex; flex-direction: column; align-items: center;
    color: var(--ink-light);
    font-family: "Oswald", "Arial Narrow", sans-serif;
    font-weight: 400;
  }
  .brand__square {
    background: var(--ink-light);
  }
  .card--back .brand { top: 28px; right: 36px; gap: 10px; }
  .card--back .brand__square { width: 54px; height: 54px; }
  .card--back .brand__name { font-size: 19px; letter-spacing: 0.3px; }

  .card--front .brand { top: 34px; left: 0; right: 0; gap: 22px; }
  .card--front .brand__square { width: 74px; height: 74px; }
  .card--front .brand__name { font-size: 40px; letter-spacing: 0.5px; line-height: 1; }

  .person {
    position: absolute; left: 60px; top: 205px;
    font-family: "Nunito", "Arial Rounded MT Bold", sans-serif;
    font-weight: 800; font-size: 54px;
    color: var(--ink-light);
    text-shadow: 2px 3px 0 var(--ink-shadow);
  }
  .contact {
    position: absolute; right: 40px; top: 135px;
    list-style: none; text-align: right;
    font-family: "Oswald", "Arial Narrow", sans-serif;
    font-weight: 300; font-size: 22px; line-height: 38px;
    color: var(--ink-light);
  }
  .tagline {
    position: absolute; left: 60px; top: 228px;
    font-family: "Nunito", "Arial Rounded MT Bold", sans-serif;
    font-weight: 800; font-size: 46px; line-height: 54px;
    color: var(--ink-light);
    text-shadow: 2px 4px 0 var(--ink-shadow);
  }
  .tagline__line--second { display: block; padding-left: 34px; }
</style>
</head>
<body>
<main class="sheet">
  <section class="card card--back" aria-label="Business card, contact side">
    <div class="card__backdrop" role="img" aria-label="Abstract pattern of overlapping translucent squares in olive, grey and purple tones"></div>
    <div class="brand">
      <span class="brand__square"></span>
      <span class="brand__name">Thornbeck Advisory Group</span>
    </div>
    <h1 class="person">Walter Pennick</h1>
    <ul class="contact">
      <li>Adress Line</li>
      <li>Email Line</li>
      <li>Phone 1 &nbsp;-&nbsp; Phone 2</li>
    </ul>
  </section>

  <section class="card card--front" aria-label="Business card, firm side">
    <div class="card__backdrop" role="img" aria-label="Abstract pattern of overlapping glowing squares in amber, teal, magenta and violet"></div>
    <div class="brand">
      <span class="brand__square"></span>
      <span class="brand__name">Thornbeck Advisory Group</span>
    </div>
    <p class="tagline">
      <span class="tagline__line">Clean Energy Procurement</span>
      <span class="tagline__line tagline__line--second">for the Public Sector</span>
    </p>
  </section>
</main>
</body>
</html>
```